Brindlequest.com is a mountain biking and climbing travel company. We need a advertisement fo...

We need a advertisement for the back cover of a guide book. We would like a simple but strong ad that includes our logo. It must state that we are a biking and climbing company and people can contact us at the web site brindlequest.com We would like you to incorparate and below photo and logo on the ad.

```html
<!DOCTYPE html>
<html lang="en">
<head>
<meta charset="utf-8">
<title>Advertisement Design job - Brindlequest.com</title>
<link rel="stylesheet" href="https://fonts.googleapis.com/css2?family=Bebas+Neue&family=Montserrat:wght@400;500;700&display=swap">
<style>
  :root {
    --board-light: #f5f5f5;
    --board-dark: #d9d9d9;
    --poster: #1f1f1f;
    --ink: #ffffff;
    --accent: #eaa829;
    --caption: #2a2a2a;
    --street-warm: #b58a55;
    --street-stone: #7a746c;
    --street-night: #3a342d;
  }
  * { margin: 0; padding: 0; box-sizing: border-box; }
  html, body { width: 1200px; height: 629px; overflow: hidden; }
  body {
    position: relative;
    background: radial-gradient(ellipse at 50% 40%, var(--board-light) 0%, var(--board-dark) 100%);
    font-family: "Montserrat", sans-serif;
    color: var(--ink);
  }
  .poster {
    position: absolute;
    top: 46px;
    width: 334px;
    height: 464px;
    background: var(--poster);
    overflow: hidden;
    box-shadow: 0 10px 14px rgba(0,0,0,0.35);
  }
  .poster--vertical { left: 44px; }
  .poster--stacked { left: 430px; }
  .poster--cutout { left: 815px; }

  .caption {
    position: absolute;
    top: 526px;
    width: 334px;
    text-align: center;
    font-size: 19px;
    color: var(--caption);
  }
  .caption--one { left: 44px; }
  .caption--two { left: 430px; }
  .caption--three { left: 815px; }
  .board-title {
    position: absolute;
    top: 578px;
    left: 0;
    width: 1200px;
    text-align: center;
    font-size: 29px;
    color: var(--caption);
    letter-spacing: 0.3px;
  }

  .photo {
    position: absolute;
    background: linear-gradient(180deg, var(--street-warm) 0%, var(--street-night) 45%, var(--street-stone) 100%);
  }

  /* Sample 1 */
  .poster--vertical .photo {
    left: 0; top: 0; width: 160px; height: 464px;
    border-top-right-radius: 16px;
    background: linear-gradient(100deg, var(--street-warm) 0%, var(--street-night) 55%, var(--street-stone) 100%);
  }
  .poster--vertical .photo-shade {
    position: absolute;
    left: 160px; top: 0; width: 174px; height: 464px;
    background: linear-gradient(180deg, #2b2926 0%, #1c1c1c 60%, #232323 100%);
  }
  .vertical-headline {
    position: absolute;
    left: 104px;
    top: 30px;
    width: 60px;
    height: 416px;
    writing-mode: vertical-rl;
    transform: rotate(180deg);
    font-family: "Bebas Neue", sans-serif;
    font-weight: 400;
    font-size: 78px;
    line-height: 60px;
    white-space: nowrap;
    text-align: center;
    color: var(--ink);
  }

  .brand {
    display: flex;
    align-items: center;
    justify-content: center;
    gap: 6px;
    font-weight: 700;
    color: var(--ink);
    letter-spacing: 1px;
  }
  .brand-dot {
    width: 14px; height: 14px;
    border-radius: 50%;
    background: var(--ink);
  }
  .tagline {
    font-size: 10px;
    line-height: 14px;
    text-align: center;
    color: var(--ink);
  }
  .web {
    font-weight: 700;
    color: var(--accent);
    text-align: center;
  }

  .poster--vertical .contact {
    position: absolute;
    left: 172px; top: 212px; width: 144px;
  }
  .poster--vertical .brand { font-size: 13px; gap: 5px; }
  .poster--vertical .brand-dot { width: 12px; height: 12px; }
  .poster--vertical .tagline { margin: 18px auto 0; width: 134px; }
  .poster--vertical .web { margin-top: 8px; font-size: 11px; }

  /* Sample 2 */
  .poster--stacked .photo {
    left: 48px; top: 0; width: 240px; height: 174px;
  }
  .stack-headline {
    position: absolute;
    left: 0; width: 334px;
    text-align: center;
    font-family: "Bebas Neue", sans-serif;
    font-weight: 400;
    white-space: nowrap;
  }
  .stack-headline--top { top: 175px; font-size: 84px; line-height: 75px; color: var(--ink); }
  .stack-headline--bottom { top: 244px; font-size: 118px; line-height: 98px; color: var(--accent); }
  .poster--stacked .tagline { position: absolute; top: 343px; left: 47px; width: 240px; }
  .poster--stacked .brand { position: absolute; top: 390px; left: 0; width: 334px; font-size: 16px; }
  .poster--stacked .web { position: absolute; top: 434px; left: 0; width: 334px; font-size: 11px; }

  /* Sample 3 */
  .cutout-headline {
    position: absolute;
    left: 0; top: 20px; width: 334px;
    text-align: center;
    font-family: "Bebas Neue", sans-serif;
    font-weight: 400;
    white-space: nowrap;
    background: linear-gradient(180deg, #d8a53f 0%, #8a6a3a 40%, #6c5a3c 70%, #5a4a30 100%);
    -webkit-background-clip: text;
    background-clip: text;
    color: transparent;
  }
  .cutout-line { display: block; }
  .cutout-line--large { font-size: 140px; line-height: 108px; letter-spacing: 6px; }
  .cutout-line--small { font-size: 100px; line-height: 86px; letter-spacing: 2px; }
  .poster--cutout .tagline { position: absolute; top: 328px; left: 62px; width: 210px; }
  .poster--cutout .brand { position: absolute; top: 385px; left: 0; width: 334px; font-size: 16px; }
  .poster--cutout .web { position: absolute; top: 434px; left: 0; width: 334px; font-size: 11px; }
</style>
</head>
<body>
  <section class="poster poster--vertical">
    <div class="photo" role="img" aria-label="Evening photo of a narrow old-town street with a cyclist blurred in motion"></div>
    <div class="photo-shade" role="img" aria-label="Darkened continuation of the street photo"></div>
    <h1 class="vertical-headline">CLIMBING+RIDING</h1>
    <div class="contact">
      <div class="brand"><span class="brand-dot"></span>BRINDLEQUEST</div>
      <p class="tagline">We are a biking and climbing company and people can contact us at</p>
      <p class="web">brindlequest.com</p>
    </div>
  </section>

  <section class="poster poster--stacked">
    <div class="photo" role="img" aria-label="Evening photo of a narrow old-town street with a cyclist blurred in motion"></div>
    <h1 class="stack-headline stack-headline--top">CLIMBING</h1>
    <h2 class="stack-headline stack-headline--bottom">RIDING</h2>
    <p class="tagline">We are a biking and climbing company and people can contact us at</p>
    <div class="brand"><span class="brand-dot"></span>BRINDLEQUEST</div>
    <p class="web">brindlequest.com</p>
  </section>

  <section class="poster poster--cutout">
    <h1 class="cutout-headline" role="img" aria-label="Headline Climbing Riding filled with the evening street photo">
      <span class="cutout-line cutout-line--large">CLIM</span>
      <span class="cutout-line cutout-line--large">BING</span>
      <span class="cutout-line cutout-line--small">RIDING</span>
    </h1>
    <p class="tagline">We are a biking and climbing company and people can contact us at</p>
    <div class="brand"><span class="brand-dot"></span>BRINDLEQUEST</div>
    <p class="web">brindlequest.com</p>
  </section>

  <p class="caption caption--one">Sample 1</p>
  <p class="caption caption--two">Sample 2</p>
  <p class="caption caption--three">Sample 3</p>
  <p class="board-title">Advertisement Design job - Brindlequest.com</p>
</body>
</html>
```